Business Card Design

We have our logo and everything in place. Looking to have a layout for our new business cards designed. These will be printed with a matte finish, possibly rounded corners, and looking to incorporate some cool spot UV layers into the design.

Ive uploaded the existing card front and back as well as our logo.

Card Size Will Be 3.5" x 2"

```html
<!DOCTYPE html>
<html lang="en">
<head>
<meta charset="utf-8">
<title>Summit Deck and Rail – Business Cards</title>
<link rel="stylesheet" href="https://fonts.googleapis.com/css2?family=Arimo:wght@400;700&display=swap">
<style>
  :root {
    --page-bg: #e9e9e9;
    --brand-blue: #3a95d8;
    --accent-blue: #2f8fd8;
    --ink-black: #0b0b0b;
    --card-white: #f4f4f4;
    --card-grey: #dcdcdc;
    --text-dark: #1d1d1d;
    --text-light: #ffffff;
  }
  * { box-sizing: border-box; margin: 0; padding: 0; }
  html, body {
    width: 1200px; height: 950px; overflow: hidden;
    background: var(--page-bg);
    font-family: "Arimo", Arial, sans-serif;
  }
  .sheet {
    position: relative; width: 1200px; height: 950px;
    display: flex; flex-direction: column; align-items: center; justify-content: center; gap: 50px;
  }
  .card {
    position: relative; width: 700px; height: 400px;
    border-radius: 28px; overflow: hidden;
    box-shadow: 0 8px 24px rgba(0,0,0,0.18);
  }

  /* Back side */
  .card-back {
    background: var(--brand-blue);
    color: var(--text-light);
    display: flex; flex-direction: column; align-items: center; justify-content: center;
  }
  .card-back .brand-name {
    font-size: 44px; font-weight: 400; letter-spacing: 1px;
    display: flex; align-items: center; gap: 14px;
  }
  .card-back .brand-mark {
    width: 16px; height: 16px; border-radius: 50%; background: var(--text-light);
  }
  .card-back .website {
    margin-top: 56px; font-size: 20px; letter-spacing: 4px;
  }

  /* Front side */
  .card-front {
    background: linear-gradient(160deg, var(--card-white) 40%, var(--card-grey) 100%);
  }
  .card-front .roof-shape { position: absolute; inset: 0; width: 100%; height: 100%; }
  .holder {
    position: absolute; top: 22px; right: 42px; text-align: right;
  }
  .holder .name { color: var(--text-light); font-size: 26px; font-weight: 700; line-height: 30px; }
  .holder .role { color: var(--accent-blue); font-size: 19px; line-height: 24px; margin-top: 4px; }
  .card-front .brand-name {
    position: absolute; left: 56px; top: 250px;
    font-size: 36px; font-weight: 400; line-height: 42px; color: var(--text-dark);
    display: flex; align-items: center; gap: 12px;
  }
  .card-front .brand-mark {
    width: 14px; height: 14px; border-radius: 50%; background: var(--text-dark);
  }
  .contact-list {
    position: absolute; left: 56px; top: 308px; list-style: none;
    font-size: 19px; color: var(--text-dark);
  }
  .contact-list li { display: flex; align-items: center; gap: 10px; height: 26px; }
  .contact-list svg { width: 16px; height: 16px; fill: var(--accent-blue); flex: none; }
</style>
</head>
<body>
<main class="sheet">

  <section class="card card-back" aria-label="Card back">
    <div class="brand-name"><span class="brand-mark"></span>Summit Deck and Rail</div>
    <div class="website">www.summitdeckandrail.com</div>
  </section>

  <section class="card card-front" aria-label="Card front">
    <svg class="roof-shape" viewBox="0 0 700 400" preserveAspectRatio="none" aria-hidden="true">
      <path d="M0,0 H700 V96 H320 L0,262 Z" fill="var(--ink-black)"/>
      <path d="M0,270 L324,102 H700 V108 H328 L0,277 Z" fill="var(--accent-blue)"/>
      <path d="M225,165 L282,132 H462 L442,147 H262 Z" fill="var(--ink-black)"/>
    </svg>

    <div class="holder">
      <div class="name">Daniel Mercer</div>
      <div class="role">President</div>
    </div>

    <div class="brand-name"><span class="brand-mark"></span>Summit Deck and Rail</div>

    <ul class="contact-list">
      <li>
        <svg viewBox="0 0 16 16"><path d="M3 1h3l1 4-2 1a9 9 0 0 0 5 5l1-2 4 1v3c0 1-1 2-2 2A13 13 0 0 1 1 3c0-1 1-2 2-2z"/></svg>
        555.010.4821
      </li>
      <li>
        <svg viewBox="0 0 16 16"><path d="M1 3h14v10H1z M1 3l7 6 7-6" fill="var(--accent-blue)" stroke="#fff" stroke-width="1"/></svg>
        summitdeckandrail@mail.com
      </li>
      <li>
        <svg viewBox="0 0 16 16"><circle cx="8" cy="8" r="7"/><path d="M1 8h14M8 1c-3 4-3 10 0 14M8 1c3 4 3 10 0 14" stroke="#fff" stroke-width="1" fill="none"/></svg>
        www.summitdeckandrail.com
      </li>
    </ul>
  </section>

</main>
</body>
</html>
```